Bi-Lingual Trash and Recycle Sign

Hello,

Pretty straight forward. I have not been able to find the exact sign we need for a property with trash and recycle guidelines. I've found close, but not complete. We are looking to have metal 12x18 street sign type signs made to provide these instructions. Attached is a sample taken from the web. I want to be sure to avoid conflicting with them so looking for the same wording but in our own. I'd also like to include our company logo, also attached in vector in horizontal and vertical for inclusion.

```html
<!DOCTYPE html>
<html lang="en">
<head>
<meta charset="utf-8">
<title>Recycle Sign – Ashbury Management</title>
<link rel="stylesheet" href="https://fonts.googleapis.com/css2?family=Roboto+Slab:wght@700;800&family=Roboto:wght@500;700;900&display=swap">
<style>
  :root {
    --green: #2f9a4c;
    --red: #c91f35;
    --maroon: #6a1e2b;
    --ink: #2b2b2b;
    --paper: #ffffff;
    --rule: #d9c9cc;
  }
  * { margin: 0; padding: 0; box-sizing: border-box; }
  html, body { width: 870px; height: 1200px; overflow: hidden; background: var(--paper); }
  .sign {
    position: relative; width: 870px; height: 1200px;
    background: var(--paper); font-family: "Roboto", Arial, sans-serif;
    display: flex; flex-direction: column; align-items: center;
  }
  .brand {
    margin-top: 70px; display: flex; align-items: center; gap: 16px;
  }
  .brand-mark { width: 52px; height: 52px; background: var(--maroon); }
  .brand-name {
    font-family: "Roboto", Arial, sans-serif; font-weight: 700;
    font-size: 40px; letter-spacing: 1px; color: var(--ink); line-height: 1;
  }
  .band {
    width: 750px; background: var(--green); color: var(--paper);
    font-family: "Roboto Slab", Georgia, serif; font-weight: 800;
    text-align: center; font-size: 104px; line-height: 120px; letter-spacing: 4px;
  }
  .band-recycle { margin-top: 50px; }
  .recycle-icon { width: 220px; height: 220px; margin: 24px 0; }
  .rules {
    margin-top: 40px; width: 750px; display: flex; justify-content: space-between;
  }
  .rule {
    flex: 1; display: flex; flex-direction: column; align-items: center;
    color: var(--red); text-align: center;
  }
  .rule + .rule { border-left: 3px solid var(--red); }
  .no-mark { display: flex; align-items: center; gap: 4px; height: 130px; }
  .no-letter { font-weight: 900; font-size: 150px; line-height: 1; }
  .no-circle { width: 118px; height: 118px; }
  .rule-text {
    margin-top: 14px; color: var(--maroon); font-weight: 900;
    font-size: 34px; line-height: 1.1; text-transform: uppercase;
  }
  .divider { width: 750px; height: 2px; background: var(--rule); margin-top: 50px; }
  .footer-line {
    margin-top: 30px; font-family: "Roboto Slab", Georgia, serif; font-weight: 700;
    color: var(--maroon); font-size: 38px; letter-spacing: 2px;
  }
  .base-strip { position: absolute; bottom: 0; left: 0; width: 100%; height: 22px; background: var(--green); }
</style>
</head>
<body>
<main class="sign">
  <header class="brand">
    <span class="brand-mark"></span>
    <span class="brand-name">ASHBURY MANAGEMENT</span>
  </header>

  <div class="band band-recycle">RECYCLE</div>

  <svg class="recycle-icon" viewBox="0 0 100 100" aria-label="Recycling arrows">
    <g fill="var(--green)">
      <g id="arrow">
        <path d="M38 18 L56 18 L66 35 L73 31 L68 50 L50 46 L57 42 L50 30 L44 40 L33 34 Z"/>
      </g>
      <use href="#arrow" transform="rotate(120 50 52)"/>
      <use href="#arrow" transform="rotate(240 50 52)"/>
    </g>
  </svg>

  <div class="band band-reciclar">RECICLAR</div>

  <section class="rules">
    <div class="rule">
      <div class="no-mark">
        <span class="no-letter">N</span>
        <svg class="no-circle" viewBox="0 0 100 100" aria-label="No plastic bags">
          <path d="M36 36 h28 l4 44 h-36 z M40 36 q0 -12 10 -12 q10 0 10 12" fill="none" stroke="#8aa7c9" stroke-width="4"/>
          <circle cx="50" cy="50" r="42" fill="none" stroke="var(--red)" stroke-width="12"/>
          <line x1="21" y1="21" x2="79" y2="79" stroke="var(--red)" stroke-width="12"/>
        </svg>
      </div>
      <p class="rule-text">Plastic<br>Bags<br>Accepted</p>
    </div>
    <div class="rule">
      <div class="no-mark">
        <span class="no-letter">N</span>
        <svg class="no-circle" viewBox="0 0 100 100" aria-label="Sin bolsas plásticas">
          <path d="M36 36 h28 l4 44 h-36 z M40 36 q0 -12 10 -12 q10 0 10 12" fill="none" stroke="#8aa7c9" stroke-width="4"/>
          <circle cx="50" cy="50" r="42" fill="none" stroke="var(--red)" stroke-width="12"/>
          <line x1="21" y1="21" x2="79" y2="79" stroke="var(--red)" stroke-width="12"/>
        </svg>
      </div>
      <p class="rule-text">Se Aceptan<br>Bolsas<br>Plásticas</p>
    </div>
  </section>

  <div class="divider"></div>
  <p class="footer-line">SINGLE SORT RECYCLING</p>
  <div class="base-strip"></div>
</main>
</body>
</html>
```